Professional Photography Business cards

I need business cards that include my logo which I have uploaded. I run a photography business. I am open to ideas but I would like one side to have my logo and the other side to have my contact info. I don't have a website made but I do own a website domain. I have uploaded 2 different logo color schemes. My business colors are Blue, black , and white.

Business Name
Business Phone Number
Business Email
Business Website address
Instagram

Industry/Entity Type

Professional Photography

Contact Information for Business Card

Phone Number: 555-314-8027 email: info@tkellan-studios.example Instagram: @t.kellanstudios website doman- www.tkellan-studios.example

Requirements
Must have
• I like the idea of a business card with a full black background front and back of card. My colors must include royal blue, black, and white

```html
<!DOCTYPE html>
<html lang="en">
<head>
<meta charset="utf-8">
<title>T. Kellan Studios — Business Card</title>
<link href="https://fonts.googleapis.com/css2?family=Lato:wght@300;400;700&display=swap" rel="stylesheet">
<style>
  :root {
    --stage: #141414;
    --card-top: #1f1f1f;
    --card-bottom: #0b0b0b;
    --ink: #f2f2f2;
    --ink-soft: #cfcfcf;
    --royal-blue: #2b5bea;
  }
  * { margin: 0; padding: 0; box-sizing: border-box; }
  html, body {
    width: 1200px; height: 800px; overflow: hidden;
    background: var(--stage);
    font-family: "Lato", sans-serif;
    color: var(--ink);
  }
  .sheet {
    width: 1200px; height: 800px;
    display: flex; align-items: center; justify-content: center; gap: 40px;
  }
  .card {
    position: relative;
    width: 520px; height: 297px;
    border-radius: 4px;
    background: linear-gradient(160deg, var(--card-top), var(--card-bottom));
    box-shadow: 0 18px 40px rgba(0,0,0,.55);
    overflow: hidden;
  }
  .card-texture {
    position: absolute; inset: 0;
    background:
      radial-gradient(circle at 55% 55%, rgba(43,91,234,.07), transparent 55%),
      radial-gradient(circle at 30% 20%, rgba(255,255,255,.03), transparent 50%);
  }
  .brand {
    display: flex; align-items: center; gap: 12px;
    font-weight: 400; color: var(--ink);
    letter-spacing: .04em; white-space: nowrap;
  }
  .brand-dot {
    flex: none;
    width: 14px; height: 14px; border-radius: 50%;
    background: var(--royal-blue);
  }
  /* front */
  .card-front .brand {
    position: absolute; top: 112px; left: 0; right: 0;
    justify-content: center; font-size: 34px;
  }
  .card-front .brand-dot { width: 26px; height: 26px; }
  .front-url {
    position: absolute; left: 0; right: 0; bottom: 50px;
    text-align: center; font-size: 13px; font-weight: 400;
    color: var(--ink-soft); letter-spacing: .06em;
  }
  /* back */
  .card-back .brand {
    position: absolute; top: 44px; right: 32px; font-size: 19px;
  }
  .identity { position: absolute; top: 44px; left: 40px; }
  .identity-name { font-size: 21px; letter-spacing: .06em; line-height: 1.1; }
  .identity-name .first { font-weight: 700; }
  .identity-name .last { font-weight: 300; }
  .identity-role {
    font-size: 11.5px; font-weight: 400; letter-spacing: .08em;
    color: var(--ink-soft); margin-top: 3px; margin-left: 4px;
  }
  .contact {
    position: absolute; left: 46px; bottom: 40px;
    list-style: none; font-size: 13px; font-weight: 400;
    color: var(--ink-soft); letter-spacing: .05em; line-height: 1.8;
  }
  .contact li { display: flex; align-items: center; gap: 8px; }
  .contact .social-mark {
    width: 9px; height: 9px; border: 1.5px solid var(--royal-blue); border-radius: 2px;
  }
</style>
</head>
<body>
  <main class="sheet">
    <section class="card card-front" aria-label="Card front">
      <div class="card-texture"></div>
      <div class="brand"><span>T. Kellan Studios</span><span class="brand-dot"></span></div>
      <p class="front-url">www.tkellan-studios.example</p>
    </section>

    <section class="card card-back" aria-label="Card back">
      <div class="card-texture"></div>
      <div class="identity">
        <p class="identity-name"><span class="first">TESSA</span> <span class="last">KELLAN</span></p>
        <p class="identity-role">OWNER/PHOTOGRAPHER</p>
      </div>
      <div class="brand"><span>T. Kellan Studios</span><span class="brand-dot"></span></div>
      <ul class="contact">
        <li>555-314-8027</li>
        <li>info@tkellan-studios.example</li>
        <li>www.tkellan-studios.example</li>
        <li><span class="social-mark"></span>@t.kellanstudios</li>
      </ul>
    </section>
  </main>
</body>
</html>
```